Book Cover Project

This is a printed journal front and back cover design. We like the current design, but it feels a little too flat / too simple.

NOTE: we are not looking for a total makeover, just a finishing / polishing of this cover.

Here is our other book cover: https://www.shelvorix.com/Mat-Studio-Blueprint-Calm-Days/dp/7390462815/ref=tmm_hrd_swatch_0?_encoding=UTF8&qid=&sr=
it's purple and yellow (mostly purple)
this one is yellow and we're thinking to add a purple bar at the bottom

Specs: 6 in x 9 in full bleed for print

```html
<!DOCTYPE html>
<html lang="en">
<head>
<meta charset="utf-8">
<title>Steady Stride Notebook – Cover</title>
<link href="https://fonts.googleapis.com/css2?family=Montserrat:wght@800&family=Raleway:wght@300;500&display=swap" rel="stylesheet">
<style>
  :root {
    --bg: #ececec;
    --yellow-light: #fee22e;
    --yellow-deep: #f7d20f;
    --ink: #222222;
    --art-tone: #ecc81a;
    --name-plate: #f3e49b;
    --purple-light: #6366b4;
    --purple-deep: #4f529f;
  }
  * { box-sizing: border-box; margin: 0; padding: 0; }
  html, body {
    width: 1200px;
    height: 960px;
    overflow: hidden;
    background: var(--bg);
  }
  .canvas {
    position: relative;
    width: 1200px;
    height: 960px;
  }
  .cover {
    position: absolute;
    left: 320px;
    top: 60px;
    width: 560px;
    height: 840px;
    background: linear-gradient(160deg, var(--yellow-light) 0%, var(--yellow-deep) 100%);
    overflow: hidden;
    color: var(--ink);
  }
  .title-line {
    position: absolute;
    left: 0;
    width: 100%;
    text-align: center;
    font-family: "Raleway", sans-serif;
    font-weight: 300;
    font-size: 57px;
    line-height: 1;
    letter-spacing: 0.14em;
    padding-left: 0.14em;
  }
  .title-top { top: 103px; }
  .title-bottom { top: 596px; }
  .title-middle {
    position: absolute;
    inset: 0;
    width: 560px;
    height: 840px;
  }
  .title-middle text {
    font-family: "Montserrat", sans-serif;
    font-weight: 800;
    font-size: 49px;
    fill: var(--ink);
  }
  .runner-art {
    position: absolute;
    top: 172px;
    width: 50px;
    height: 152px;
    background: var(--art-tone);
    border-radius: 24px 24px 8px 8px;
    opacity: 0.55;
  }
  .runner-art-left { left: 195px; }
  .runner-art-right { left: 304px; }
  .tagline {
    position: absolute;
    top: 668px;
    left: 0;
    width: 100%;
    text-align: center;
    font-family: "Raleway", sans-serif;
    font-weight: 500;
    font-size: 19px;
    letter-spacing: 0.04em;
  }
  .author-plate {
    position: absolute;
    left: 187px;
    top: 729px;
    width: 186px;
    height: 37px;
    background: var(--name-plate);
    display: flex;
    align-items: center;
    justify-content: center;
    font-family: "Raleway", sans-serif;
    font-weight: 500;
    font-size: 13.5px;
    letter-spacing: 0.06em;
  }
  .bottom-bar {
    position: absolute;
    left: 0;
    bottom: 0;
    width: 100%;
    height: 30px;
    background: linear-gradient(90deg, var(--purple-light), var(--purple-deep));
  }
</style>
</head>
<body>
  <div class="canvas">
    <div class="cover">
      <div class="title-line title-top">STEADY</div>

      <div class="runner-art runner-art-left" role="img" aria-label="Single-line drawing of a runner facing forward"></div>
      <div class="runner-art runner-art-right" role="img" aria-label="Single-line drawing of a runner facing forward"></div>

      <svg class="title-middle" viewBox="0 0 560 840" aria-label="Stride">
        <text transform="translate(293,373) rotate(-90)" text-anchor="middle" textLength="390" lengthAdjust="spacing">STRIDE</text>
      </svg>

      <div class="title-line title-bottom">NOTEBOOK</div>
      <div class="tagline">Move - Reflect - Grow</div>

      <div class="author-plate">ELIAS BROOKFIELD</div>

      <div class="bottom-bar"></div>
    </div>
  </div>
</body>
</html>
```